Torvane Travel Business Card Design

We need a new business card design for our travel agency business - Torvane Travel. We design packages to some of the most popular travel destinations in the world for groups, individuals and also tailor-make personalised packages. Our logo attached must be used. On the back of the card we would like a list of all websites under our Torvane brand to be posted. We would like clean, modern, simple design.

Industry/Entity Type

Travel Agent

Contact Information for Business Card

Owen Pridmore
National Sales Manager
Reservations: 1300 742 689
Tel: 61 28473 5096
Fax: 61 2847 3971
Email: owen@torvanetravel.com.au
Web: www.torvanetravel.com.au

Address: Level 1, 417 Harwick Street
Sydney NSW 2000 Australia

Requirements
Must have
• On the back of the card we want all websites listed under our Torvane brand.
• Torvane Travel Group - Wholesale Specialists
• www.qpjourneys.com.au - New Caledonia
• www.bravelmijourneys.com.au - Tahiti
• www.sorvenbreakhub.com.au - China
Nice to have
• Modern, clean lined, simple and fresh
Should not have
• Look dull

```html
<!DOCTYPE html>
<html lang="en">
<head>
<meta charset="utf-8">
<title>Torvane Travel – Business Card</title>
<link rel="stylesheet" href="https://fonts.googleapis.com/css2?family=Roboto+Condensed:wght@400;700&display=swap">
<style>
  :root {
    --backdrop: #cfd6d5;
    --card-white: #ffffff;
    --brand-blue: #1e2ea3;
    --back-blue: #0b1fb5;
    --brand-red: #e6395e;
    --text-white: #ffffff;
    --shadow: rgba(40, 50, 60, 0.18);
  }
  * { margin: 0; padding: 0; box-sizing: border-box; }
  html, body {
    width: 1200px; height: 1000px; overflow: hidden;
    background: var(--backdrop);
    font-family: "Roboto Condensed", "Arial Narrow", sans-serif;
  }
  .canvas { position: relative; width: 1200px; height: 1000px; }

  .card {
    position: absolute;
    width: 640px; height: 388px;
    box-shadow: 0 6px 18px var(--shadow);
  }
  .card--front { left: 110px; top: 90px; background: var(--card-white); }
  .card--back  { left: 450px; top: 520px; background: var(--back-blue); }

  .brand {
    position: absolute;
    display: flex; align-items: center; gap: 10px;
    font-weight: 700; font-size: 40px; letter-spacing: -0.5px; line-height: 1;
  }
  .brand__dot { width: 14px; height: 14px; border-radius: 50%; }
  .card--front .brand { left: 44px; top: 160px; color: var(--brand-blue); }
  .card--front .brand__dot { background: var(--brand-blue); }
  .card--back .brand { right: 44px; top: 88px; color: var(--text-white); }
  .card--back .brand__dot { background: var(--text-white); }

  .contact {
    position: absolute; left: 350px; top: 44px;
    color: var(--brand-blue); font-size: 17px; line-height: 1.3;
  }
  .contact__name { color: var(--brand-red); font-weight: 700; font-size: 19px; }
  .contact__title { font-weight: 700; font-size: 19px; }
  .contact__group { margin-top: 30px; }

  .front-web {
    position: absolute; left: 44px; bottom: 36px;
    color: var(--brand-red); font-weight: 700; font-size: 17px;
  }

  .site-list {
    position: absolute; right: 44px; bottom: 44px;
    list-style: none; text-align: right;
    color: var(--text-white); font-weight: 700; font-size: 18px; line-height: 1.35;
  }
  .site-list__dest { color: var(--brand-red); text-transform: uppercase; }
</style>
</head>
<body>
<main class="canvas">

  <section class="card card--front" aria-label="Card front">
    <div class="brand"><span class="brand__dot"></span>Torvane Travel</div>

    <div class="contact">
      <p class="contact__name">Owen Pridmore</p>
      <p class="contact__title">National Sales Manager</p>
      <p>owen@torvanetravel.com.au</p>

      <div class="contact__group">
        <p>Reservations: 1300 742 689</p>
        <p>Tel: 61 28473 5096</p>
        <p>Fax: 61 2847 3971</p>
      </div>

      <div class="contact__group">
        <p>Level 1, 417 Harwick Street</p>
        <p>Sydney NSW 2000 Australia</p>
      </div>
    </div>

    <p class="front-web">www.torvanetravel.com.au</p>
  </section>

  <section class="card card--back" aria-label="Card back">
    <div class="brand"><span class="brand__dot"></span>Torvane Travel</div>

    <ul class="site-list">
      <li>www.bravelmijourneys.com.au - <span class="site-list__dest">Tahiti</span></li>
      <li>www.sorvenbreakhub.com.au - <span class="site-list__dest">China</span></li>
      <li>www.qpjourneys.com.au - <span class="site-list__dest">New Caledonia</span></li>
    </ul>
  </section>

</main>
</body>
</html>
```